Vel-Trax.ch is looking for business card letterhead and envelope C5 with WOW effect

We need a strong business card for our company Vel-Trax.ch, logo is available. You want a black or dark background on which the logo Stark r% 26 # 252; appears. Letterhead and envelope in C5 format should be in a similar design, but does not have to be We need a strong business card for our company Vel-Trax.ch, logo is available. A black or dark background is desired, on which the logo Stark comes across. The letterhead and the envelope in C5 format should have a similar design.

Target Market(s)

Private customers as well as entrepreneurs

Contact Information for Business Card

E-mail: info@vel-trax.ch
Web.www.Vel-Trax.ch
Tel: +41 ( 0 ) 79 684 3027
Adresse:
Lindenhaldeweg 14
9418 Brenzikon

Hier kann man Icons verwenden für Email,Tel und Adressse

Font styles to use
Other font styles liked:
• Dubai,bold

Colors

Designer to choose colors to be used in the design.

Requirements
Must have
• WOW effect
Nice to have
• R% 26 # 252; back business card with our service listings. - VEHICLE LABELING - SHOP WINDOW LABELING - STICKERS AND MUCH MORE ... in red color

```html
<!DOCTYPE html>
<html lang="en">
<head>
<meta charset="utf-8">
<title>Vel-Trax.ch Business Card</title>
<link rel="stylesheet" href="https://fonts.googleapis.com/css2?family=Roboto:wght@300;400;500;700&display=swap">
<style>
  :root {
    --backdrop: #2a2a2a;
    --card: #1f1f1f;
    --accent: #f7c318;
    --text: #e8e8e8;
    --rule: #6a6a6a;
  }
  * { margin: 0; padding: 0; box-sizing: border-box; }
  html, body { width: 1200px; height: 880px; overflow: hidden; }
  body {
    background: var(--backdrop);
    font-family: "Roboto", Arial, sans-serif;
    position: relative;
  }
  .card {
    position: absolute;
    width: 600px;
    height: 360px;
    background: var(--card);
    border-radius: 18px;
    border-bottom: 8px solid var(--accent);
    box-shadow: 0 18px 40px rgba(0,0,0,.45);
    overflow: hidden;
  }
  .card--front { left: 70px; top: 50px; }
  .card--back { left: 530px; top: 470px; }

  .brand {
    position: absolute;
    left: 50px;
    top: 160px;
    display: flex;
    align-items: center;
    gap: 12px;
  }
  .brand__mark {
    width: 40px; height: 40px;
    background: var(--accent);
    border-radius: 4px;
  }
  .brand__name {
    color: var(--text);
    font-weight: 700;
    font-size: 24px;
    letter-spacing: 1px;
  }
  .divider {
    position: absolute;
    left: 325px;
    top: 80px;
    width: 1px;
    height: 200px;
    background: var(--rule);
  }
  .details {
    position: absolute;
    left: 355px;
    top: 90px;
    color: var(--text);
  }
  .services__title {
    color: var(--accent);
    font-weight: 500;
    font-size: 26px;
    margin-bottom: 10px;
  }
  .services__list { list-style: none; }
  .services__item {
    font-size: 14px;
    font-weight: 300;
    letter-spacing: .3px;
    line-height: 26px;
    display: flex;
    align-items: center;
    gap: 10px;
  }
  .services__item::before {
    content: "";
    width: 8px; height: 8px;
    border-radius: 50%;
    background: var(--accent);
  }
  .person__name {
    color: var(--accent);
    font-weight: 500;
    font-size: 26px;
  }
  .person__role {
    font-size: 15px;
    font-weight: 300;
    margin-bottom: 16px;
  }
  .contact { list-style: none; }
  .contact__row {
    display: flex;
    align-items: flex-start;
    gap: 12px;
    font-size: 15px;
    font-weight: 300;
    line-height: 21px;
  }
  .contact__row--spaced { margin-bottom: 12px; }
  .contact__icon { width: 14px; height: 14px; margin-top: 3px; flex: none; }
  .contact__hl { color: var(--accent); }
</style>
</head>
<body>

  <section class="card card--front">
    <div class="brand">
      <span class="brand__mark"></span>
      <span class="brand__name">VEL-TRAX.CH</span>
    </div>
    <div class="divider"></div>
    <div class="details services">
      <h2 class="services__title">our service listings</h2>
      <ul class="services__list">
        <li class="services__item">VEHICLE LABELING</li>
        <li class="services__item">SHOP WINDOW LABELING</li>
        <li class="services__item">STICKERS AND MUCH MORE</li>
      </ul>
    </div>
  </section>

  <section class="card card--back">
    <div class="brand">
      <span class="brand__mark"></span>
      <span class="brand__name">VEL-TRAX.CH</span>
    </div>
    <div class="divider"></div>
    <div class="details person">
      <h2 class="person__name">Marlon Keller</h2>
      <p class="person__role">Manager</p>
      <ul class="contact">
        <li class="contact__row contact__row--spaced">
          <svg class="contact__icon" viewBox="0 0 14 14"><path d="M7 0a5 5 0 0 0-5 5c0 3.5 5 9 5 9s5-5.5 5-9a5 5 0 0 0-5-5zm0 7a2 2 0 1 1 0-4 2 2 0 0 1 0 4z" fill="var(--accent)"/></svg>
          <span>Lindenhaldeweg 14<br>9418 Brenzikon</span>
        </li>
        <li class="contact__row">
          <svg class="contact__icon" viewBox="0 0 14 14"><path d="M3 1l2 3-1.3 1.3a8 8 0 0 0 5 5L10 9l3 2-1.5 2.5C6 13 1 8 .5 2.5z" fill="var(--accent)"/></svg>
          <span>+41 ( 0 ) 79 684 3027</span>
        </li>
        <li class="contact__row">
          <svg class="contact__icon" viewBox="0 0 14 14"><rect x="0.5" y="2.5" width="13" height="9" fill="var(--accent)"/><path d="M1 3l6 5 6-5" stroke="var(--card)" stroke-width="1.2" fill="none"/></svg>
          <span>info@vel-trax.ch</span>
        </li>
        <li class="contact__row">
          <svg class="contact__icon" viewBox="0 0 14 14"><circle cx="7" cy="7" r="6" fill="none" stroke="var(--accent)" stroke-width="1.5"/><path d="M1 7h12M7 1c-3 3-3 9 0 12M7 1c3 3 3 9 0 12" stroke="var(--accent)" fill="none"/></svg>
          <span>www.<span class="contact__hl">Vel-Trax</span>.ch</span>
        </li>
      </ul>
    </div>
  </section>

</body>
</html>
```